Interimsmanager sucht Design
Zielgruppe
Erbringen von Dienstleistungen in Form Interimsmanagement in Krankenhäusern in den Bereichen IT, Medizintechnik, Projektmanagement
Zielgruppe: Vorstände, Bereichsleiter, Entscheider für IT und Medizintechnik und Kosten
Branchen: Krankenhäuser, IT, Dienstleistung
Aufgabenstellung
1) Flyer DIN A 4 6seitig (2-Bruch-Wickel-Falz)
2) Texte und grobe Layout-Vorgabe in anhängendem PDF (siehe auch 6)
3) erforderliche Fotos z.B. aus Portalen wie Bildora Platzhalter/Preview einsetzen, die Lizenzen werden dann von mir gekauft
4) Alternativ-Vorschläge bei Bildauswahl willkommen
5) 1 Profilbild je nach Platz/Layout einbauen
6) Logo-Vorlage in diversen Formaten, kann auch noch für 300dpi aufbereitet werden (derzeit noch nicht vorhanden)
6) anhängendes Dokument gibt nur grob vor, wie so etwas aussehen könnte - Alternativ-Vorschläge willkommen

```html
<!DOCTYPE html>
<html lang="de">
<head>
<meta charset="utf-8">
<title>Kestrelhaus – Flyer Innenseiten</title>
<link href="https://fonts.googleapis.com/css2?family=Montserrat:ital,wght@0,300;0,400;0,600;0,700;1,300;1,400&display=swap" rel="stylesheet">
<style>
  :root{
    --stage:#e4e4e4;
    --blue:#1f6db0;
    --blue-deep:#18588f;
    --teal-dark:#1b4f63;
    --teal-text:#2b93bd;
    --teal-head:#1d6a86;
    --ink:#3a3a3a;
    --paper:#f6f6f6;
    --photo-a:#b9b9b9;
    --photo-b:#6f6f6f;
    --badge:#9a9a9a;
    --white:#ffffff;
  }
  *{box-sizing:border-box;margin:0;padding:0}
  html,body{width:1200px;height:900px;overflow:hidden}
  body{background:var(--stage);font-family:"Montserrat",sans-serif;position:relative}

  .spread{position:absolute;left:190px;top:30px;width:820px;height:840px;display:flex;gap:20px}
  .panel{width:400px;height:840px;position:relative;overflow:hidden}

  /* left panel */
  .panel--benefits{background:linear-gradient(180deg,var(--blue) 0%,var(--blue-deep) 100%);color:var(--white)}
  .panel__photo{width:100%;height:200px;background:linear-gradient(160deg,var(--photo-a),var(--photo-b))}
  .brand-band{position:absolute;top:170px;left:0;width:100%;height:86px;background:var(--teal-dark);
    display:flex;align-items:center;padding:0 32px}
  .brand-band__name{font-size:30px;font-weight:400;letter-spacing:.5px;color:var(--white)}
  .benefits{padding:82px 32px 0}
  .benefits__title{font-size:22px;font-weight:300;line-height:1.2}
  .benefits__lead{margin-top:12px;font-size:12.5px;font-weight:700;line-height:1.4}
  .benefits__question{margin-top:26px;font-size:21px;font-weight:300;line-height:1.2;color:rgba(255,255,255,.55)}
  .benefits__list{margin-top:20px;list-style:none;font-size:12.5px;line-height:1.45}
  .benefits__list li{position:relative;padding-left:16px;margin-bottom:7px}
  .benefits__list li::before{content:"";position:absolute;left:2px;top:7px;width:5px;height:5px;border-radius:50%;background:var(--white)}

  /* right panel */
  .panel--profile{background:linear-gradient(180deg,var(--paper),#e2e2e2);color:var(--ink)}
  .panel--profile .panel__photo{height:230px;background:linear-gradient(160deg,#d6d6d6,#8a8a8a)}
  .profile-band{position:absolute;top:150px;left:0;width:100%;height:90px;background:var(--teal-dark);padding:10px 28px}
  .profile-band__title{font-size:30px;font-weight:300;line-height:1.1;color:var(--white);letter-spacing:.5px}
  .profile{padding:28px 28px 0}
  .profile__intro{font-size:12px;font-style:italic;font-weight:400;color:var(--teal-text);line-height:1.45}
  .profile__claim{margin-top:10px;font-size:12px;font-style:italic;color:var(--teal-text)}
  .profile__contact{margin-top:22px;font-size:12px;font-weight:700;color:var(--teal-head)}
  .profile__list{margin-top:10px;list-style:none;font-size:11.5px;line-height:1.45}
  .profile__list li{position:relative;padding-left:14px;margin-bottom:3px}
  .profile__list li::before{content:"•";position:absolute;left:2px;top:0}
  .quote{position:relative;margin-top:24px;padding:0 30px 0 26px}
  .quote__mark{position:absolute;font-size:56px;font-weight:700;color:var(--teal-head);line-height:1}
  .quote__mark--open{left:0;top:-14px}
  .quote__mark--close{right:10px;bottom:-52px}
  .quote__text{font-size:15px;font-style:italic;font-weight:300;color:var(--teal-text);line-height:1.35}
  .references{margin-top:40px;text-align:center}
  .references__title{font-size:12px;font-weight:700;color:var(--teal-head)}
  .references__grid{margin-top:18px;display:grid;grid-template-columns:1fr 1fr;gap:20px 40px;justify-items:center}
  .reference-badge{width:100px;height:44px;border-radius:8px;background:var(--badge)}
</style>
</head>
<body>
<main class="spread">
  <section class="panel panel--benefits">
    <div class="panel__photo" role="img" aria-label="Schwarzweißfoto: Geschäftsleute im Gespräch, vorne eine lächelnde Frau"></div>
    <div class="brand-band">
      <span class="brand-band__name">Kestrelhaus</span>
    </div>
    <div class="benefits">
      <h1 class="benefits__title">Interimsmanagement in IT und Medizintechnik</h1>
      <p class="benefits__lead">Maßgeschneiderte B2B-Lösungen für Ihr Unternehmen, um Ihre unternehmenspolitischen Zielsetzungen konsequent umzusetzen.</p>
      <h2 class="benefits__question">Welche Vorteile bietet Ihnen Interims Management für Ihr Haus?</h2>
      <ul class="benefits__list">
        <li>Breit gefächerte Fachexpertise</li>
        <li>Definierte Kalkulationsrahmen ohne Belastung Ihres Headcounts und der Personalkosten</li>
        <li>Fest umrissene Kosten ohne Nachteil einer festen arbeitsvertraglichen Bindung</li>
        <li>Entlastung der Geschäftsführung</li>
        <li>Zusätzliche Ressourcen für Ihr Unternehmen</li>
        <li>Flexibilität und Effizienz</li>
        <li>Kurzfristige Verfügbarkeit</li>
        <li>Unternehmenspolitische Unabhängigkeit</li>
      </ul>
    </div>
  </section>

  <section class="panel panel--profile">
    <div class="panel__photo" role="img" aria-label="Schwarzweißes Porträtfoto des Ansprechpartners mit Brille im Anzug"></div>
    <div class="profile-band">
      <h2 class="profile-band__title">Kestrelhaus<br>Business —</h2>
    </div>
    <div class="profile">
      <p class="profile__intro">Ihr durchsetzungsstarker und erfahrener Spezialist für alle Fragen rund um Medizin-IT und Medizintechnik</p>
      <p class="profile__claim">Innovation und Kompetenz für die klinische Praxis</p>
      <p class="profile__contact">Ihr Ansprechpartner: Dr. Lorenz Haberkamp</p>
      <ul class="profile__list">
        <li>Facharzt für Orthopädie</li>
        <li>Medizininformatiker</li>
        <li>Mit über 20 Jahren Expertise in der Medizintechnik und Medizininformatik und im Projektmanagement</li>
        <li>Interdisziplinäre Betrachtung Ihrer Geschäftsprozesse</li>
      </ul>
      <blockquote class="quote">
        <span class="quote__mark quote__mark--open">“</span>
        <p class="quote__text">Lorem ipsum dolor sit amet, consectetuer adipiscing elit, sed diam nonummy nibh.</p>
        <span class="quote__mark quote__mark--close">”</span>
      </blockquote>
      <div class="references">
        <p class="references__title">Auszug aus unseren Referenzen</p>
        <div class="references__grid">
          <span class="reference-badge"></span>
          <span class="reference-badge"></span>
          <span class="reference-badge"></span>
          <span class="reference-badge"></span>
        </div>
      </div>
    </div>
  </section>
</main>
</body>
</html>
```